Pruett Family Motto/Mission Statement

We are creating a poster to be hung in our home with several purpose statements for our family (last name Pruett, and "The Pruett Family" should be included in the poster prominently). The text that we want included is in the attached file.

Our kids range in age from 8 to 17, so we are looking for something that is homey and cheerful, but fairly bold and oriented to older kids (and not so much younger kids).

I've attached a couple of example poster/statements that we generally like. Overall color scheme could include blues and greens and possibly some brown.

Anticipated size of this poster would be 18"x24" with a portrait orientation.

```html
<!DOCTYPE html>
<html lang="en">
<head>
<meta charset="utf-8">
<title>The Pruett Family</title>
<link rel="stylesheet" href="https://fonts.googleapis.com/css2?family=Amaranth:wght@700&family=Fira+Sans:wght@300;700&display=swap">
<style>
  :root {
    --ink: #0a0a5c;
    --glow: rgba(255, 255, 255, 0.95);
    --bg-light: #e4f3fb;
    --bg-mid: #a9d8f2;
    --bg-deep: #7f98d8;
    --rule: rgba(90, 110, 170, 0.45);
    --frame: #8d93a8;
  }
  * { margin: 0; padding: 0; box-sizing: border-box; }
  html, body { width: 901px; height: 1200px; overflow: hidden; }
  body { background: #ffffff; }

  .poster {
    position: relative;
    width: 901px;
    height: 1200px;
    overflow: hidden;
    border: 1.5px solid var(--frame);
  }

  .backdrop {
    position: absolute;
    inset: 0;
    background:
      radial-gradient(circle at 48% 52%, var(--bg-light) 0%, var(--bg-mid) 38%, transparent 70%),
      radial-gradient(circle at 90% 8%, var(--bg-deep) 0%, transparent 35%),
      radial-gradient(circle at 5% 90%, var(--bg-deep) 0%, transparent 30%),
      linear-gradient(160deg, #b8c8ee 0%, #bfe6f7 45%, #a7c0ec 100%);
  }

  .rules { position: absolute; inset: 0; }

  .title {
    position: absolute;
    top: 104px;
    left: 0;
    width: 901px;
    display: flex;
    justify-content: center;
    align-items: center;
    color: var(--ink);
    font-family: "Fira Sans", sans-serif;
    text-shadow: 0 0 8px var(--glow), 0 0 3px var(--glow);
  }
  .title-the {
    font-weight: 300;
    font-size: 32px;
    transform: rotate(-90deg);
    width: 30px;
    margin-right: 6px;
    margin-top: 10px;
  }
  .title-name {
    font-weight: 700;
    font-size: 88px;
    letter-spacing: -2px;
    line-height: 1;
  }

  .statement {
    position: absolute;
    left: 0;
    width: 901px;
    text-align: center;
    font-family: "Amaranth", sans-serif;
    font-weight: 700;
    font-size: 32px;
    line-height: 40px;
    color: var(--ink);
    text-shadow: 0 0 7px var(--glow), 0 0 3px var(--glow), 0 0 1px var(--glow);
  }
</style>
</head>
<body>
<main class="poster">
  <div class="backdrop" role="img" aria-label="Soft blue abstract technology background with glowing circles and squares"></div>

  <svg class="rules" width="901" height="1200" viewBox="0 0 901 1200" aria-hidden="true">
    <g stroke="var(--rule)" stroke-width="1.5">
      <line x1="77" y1="112" x2="826" y2="112"/>
      <line x1="77" y1="213" x2="826" y2="213"/>
      <line x1="189" y1="387" x2="706" y2="387"/>
      <line x1="189" y1="503" x2="706" y2="503"/>
      <line x1="189" y1="615" x2="706" y2="615"/>
      <line x1="189" y1="769" x2="706" y2="769"/>
      <line x1="189" y1="843" x2="706" y2="843"/>
      <line x1="189" y1="984" x2="706" y2="984"/>
    </g>
  </svg>

  <h1 class="title">
    <span class="title-the">The</span>
    <span class="title-name">Pruett Family</span>
  </h1>

  <p class="statement" style="top:285px">We love<br>to LEARN new things.</p>
  <p class="statement" style="top:405px">We look at life<br>through a POSITIVE lens.</p>
  <p class="statement" style="top:521px">KINDNESS guides<br>our words and deeds.</p>
  <p class="statement" style="top:630px">We create ADVENTURE<br>and choose<br>experiences over things.</p>
  <p class="statement" style="top:784px">We commit to be FIT.</p>
  <p class="statement" style="top:851px">Our days<br>are brightened<br>BY A SENSE OF HUMOR.</p>
  <p class="statement" style="top:1000px">We DO WHAT IS RIGHT<br>even when no one is watching.</p>
</main>
</body>
</html>
```